Geschäftspapiere für jungen Rechtsanwalt
Zielgruppe
'Vohrmann' Rechtsanwaltskanzlei, die hauptsächlich im Verkehrsrecht tätig ist. Dabei sowohl für Otto-Normalbürger, als auch für Versicherungen.
Aufgabenstellung
Neben Postanschrift, Telefon, Faxnummer und E-Mail-Adresse sind Angaben zur Bankverbindung und Steuernummer erforderlich.
Bitte keine Klassiker, wie z.B. Paragraphenzeichen, Justizia, etc.

```html
<!DOCTYPE html>
<html lang="de">
<head>
<meta charset="utf-8">
<title>Vohrmann Rechtsanwaltskanzlei – Geschäftspapiere</title>
<link href="https://fonts.googleapis.com/css2?family=Barlow:wght@400;500&family=Arimo:wght@400;700&display=swap" rel="stylesheet">
<style>
  :root{
    --brand:#5f6e74;
    --ink:#5f6e74;
    --muted:#9aa3a7;
    --paper:#ffffff;
    --mark:#8a8a8a;
  }
  html,body{margin:0;padding:0;width:1200px;height:840px;overflow:hidden;background:var(--paper);}
  svg{display:block;}
  .sheet{fill:var(--paper);filter:drop-shadow(4px 5px 3px rgba(0,0,0,.55));}
  .band{fill:var(--brand);}
  .crop{stroke:var(--mark);stroke-width:.7;fill:none;}
  .crop-dash{stroke:var(--mark);stroke-width:.7;stroke-dasharray:5 5;fill:none;}
  .fold{stroke:var(--ink);stroke-width:.7;}
  .window-frame{stroke:var(--ink);stroke-width:.7;fill:none;}
  .wordmark{font-family:"Barlow",sans-serif;font-weight:500;letter-spacing:.04em;}
  .wordmark.on-band{fill:#fff;}
  .wordmark.on-paper{fill:var(--brand);}
  .tagline{font-family:"Barlow",sans-serif;font-weight:400;fill:#fff;letter-spacing:.02em;}
  .tagline.dark{fill:var(--brand);}
  .person{font-family:"Arimo",sans-serif;font-weight:700;fill:var(--ink);letter-spacing:.02em;}
  .detail{font-family:"Arimo",sans-serif;font-weight:400;fill:var(--ink);}
  .detail.strong{font-weight:700;}
  .detail.light{fill:var(--muted);}
  .envelope-window{fill:var(--paper);stroke:#d0d0d0;stroke-width:1;filter:drop-shadow(0 3px 3px rgba(0,0,0,.35));}
</style>
</head>
<body>
<svg width="1200" height="840" viewBox="0 0 1200 840" xmlns="http://www.w3.org/2000/svg">

  <g class="crop">
    <path d="M53 7v30M563 7v30M53 790v30M563 790v30"/>
    <path d="M7 54h30M579 54h30M7 774h30M579 774h30"/>
    <path d="M626 405h30M1135 405h30M1168 774h30"/>
    <path d="M626 785v30M1160 785v30M626 462v20M1160 462v20"/>
    <path d="M665 405l16-25M1120 405l-16-25"/>
  </g>
  <path class="crop-dash" d="M587 507h40M1160 507h40"/>

  <g class="letterhead">
    <rect class="sheet" x="53" y="54" width="510" height="720"/>
    <rect class="band" x="51" y="85" width="368" height="30"/>
    <rect class="band" x="481" y="85" width="82" height="30"/>
    <text class="wordmark on-band" x="85" y="107" font-size="15">VOHRMANN</text>
    <text class="tagline" x="178" y="106" font-size="8">Rechtsanwaltskanzlei</text>

    <g class="sender-block">
      <text class="person" x="426" y="100" font-size="6.5">Jonas Wendler</text>
      <text class="detail" x="426" y="107" font-size="5">Rechtsanwalt</text>
      <text class="detail strong" x="426" y="120" font-size="5.2">Kontakt</text>
      <text class="detail" x="426" y="127" font-size="5">Tel&#160;&#160;&#160;&#160;&#160;&#160;+49 (0 61 1) 24 70</text>
      <text class="detail" x="426" y="134" font-size="5">Fax&#160;&#160;&#160;&#160;&#160;&#160;+49 (0 61 1) 24 71 88</text>
      <text class="detail" x="426" y="141" font-size="5">Mobil&#160;&#160;+49 (0 17 2) 58 30 46</text>
      <text class="detail strong" x="426" y="154" font-size="5.2">Brightway Partners Ltd. – London – Wiesbaden</text>
      <text class="detail" x="426" y="161" font-size="5">Niederlassung Deutschland</text>
      <text class="detail" x="426" y="167" font-size="5">Lindenallee 14</text>
      <text class="detail" x="426" y="174" font-size="5">65183 Wiesbaden</text>
      <text class="detail light" x="426" y="189" font-size="5">Amtsgericht Talheim</text>
      <text class="detail light" x="426" y="196" font-size="5">Handelsregister: 0031872</text>
      <text class="detail light" x="426" y="202" font-size="5">USt. –ID-Nr.: DE0007281940</text>
      <text class="detail light" x="426" y="219" font-size="5">Bank: Rheinbank Mitte</text>
      <text class="detail light" x="426" y="226" font-size="5">IBAN: DE 12 40020050 3100458822</text>
      <text class="detail light" x="426" y="232" font-size="5">BIC-Swift: RHBMDEFFXXX</text>
    </g>

    <g class="address-window">
      <path class="window-frame" d="M99 167v-10a7 7 0 0 1 7-7h10M294 150h10a7 7 0 0 1 7 7v10M99 235v10a7 7 0 0 0 7 7h10M294 252h10a7 7 0 0 0 7-7v-10"/>
      <text class="wordmark on-paper" x="119" y="168" font-size="6.5">VOHRMANN</text>
      <text class="detail light" x="159" y="168" font-size="4.8">•&#160; Am Weinberg 3 &#160;•&#160; 64340 Talheim-Obermühl</text>
    </g>
    <path class="fold" d="M62 301h10M62 544h10"/>
  </g>

  <g class="business-card">
    <rect class="sheet" x="649" y="113" width="251" height="147"/>
    <rect class="band" x="649" y="167" width="14" height="30"/>
    <rect class="band" x="721" y="167" width="179" height="30"/>
    <text class="wordmark on-band" x="781" y="190" font-size="16">VOHRMANN</text>
    <text class="person" x="669" y="181" font-size="6.2">Jonas Wendler</text>
    <text class="detail" x="669" y="188" font-size="5">Rechtsanwalt</text>
    <text class="detail strong" x="669" y="201" font-size="5.2">Kontakt</text>
    <text class="detail" x="669" y="207" font-size="5">Tel&#160;&#160;&#160;&#160;&#160;&#160;+49 (0 61 1) 24 70</text>
    <text class="detail" x="669" y="214" font-size="5">Fax&#160;&#160;&#160;&#160;&#160;&#160;+49 (0 61 1) 24 71 88</text>
    <text class="detail" x="669" y="220" font-size="5">Mobil&#160;&#160;+49 (0 17 2) 58 30 46</text>
    <text class="detail strong" x="669" y="234" font-size="5.2">Brightway Partners Ltd. – London – Wiesbaden</text>
    <text class="detail" x="669" y="241" font-size="5">Niederlassung Deutschland</text>
    <text class="detail" x="669" y="247" font-size="5">Lindenallee 14</text>
    <text class="detail" x="669" y="254" font-size="5">65183 Wiesbaden</text>
  </g>

  <g class="business-card back">
    <rect class="sheet" x="910" y="113" width="251" height="147"/>
    <rect class="band" x="910" y="167" width="21" height="30"/>
    <rect class="band" x="1012" y="167" width="149" height="30"/>
    <text class="wordmark on-paper" x="971" y="186" font-size="11" text-anchor="middle">VOHRMANN</text>
    <text class="tagline" x="1086" y="185" font-size="8" text-anchor="middle">Rechtsanwaltskanzlei</text>
  </g>

  <g class="envelope">
    <path class="sheet" d="M657 405H1118a14 14 0 0 1 12 9L1160 507H626Z"/>
    <text class="wordmark on-paper" x="0" y="0" font-size="15" text-anchor="middle" transform="translate(925 449) rotate(180)">VOHRMANN</text>
    <rect class="sheet" x="626" y="507" width="534" height="267"/>
    <rect class="band" x="626" y="542" width="48" height="29"/>
    <rect class="band" x="797" y="542" width="363" height="29"/>
    <text class="wordmark on-paper" x="683" y="566" font-size="18">VOHRMANN</text>
    <text class="tagline dark" x="717" y="577" font-size="6">Rechtsanwaltskanzlei</text>
    <rect class="envelope-window" x="679" y="615" width="242" height="108" rx="9"/>
  </g>
</svg>
</body>
</html>
```